High-end Oceanfront Real Estate Group Needs Clean, Modern Web Design

I’m looking for a clean, professional, modern and beautiful homepage web design for a Real Estate group in Southern California, USA.

The group/company is “Marlow on the Shore,” and they specialize in high end (i.e. expensive), oceanfront real estate in the Orange County area.

The look and feel of the page should accentuate the brand qualities: luxurious/expensive, professional, and beautiful (Orange County is one of the most beautiful areas in all the US and we would love the site to emphasize the beautiful beaches and scenery it has to offer).

Looks we like:
• www.brantleyhomesrealty.example
• www.keptbyfenwick.example -- I think the design is pretty out-dated in this site, but I like the organization/layout of the site

Header Tags (I don’t know if we can fit all of these, may need a side-menu, but I’d prefer header title only if possible):
• Welcome
• Featured Listings
• Previously Sold
• Sell
• Property Search
• Team
• Videos
• Blog
• Explore O.C.
• Contact

I have attached the beach and logo pics that we would like to use as the header, a few pictures of the team, and one sample home/view pic which can be used in any of the other sections (for pictures of the homes, just find expensive oceanfront houses and that will be fine).

I promise to provide feedback to each and every design submission. I appreciate the hard work that all of you are putting into your designs. There can be only one contest winner, but I hope to give all of you helpful feedback to submit the best designs possible!

Target Market(s)

Very wealthy home owners of oceanfront properties. These properties are worth several millions of dollars, and thus the site and brand needs to be targeted to very wealthy, successful individuals and families (both US and international buyers).

Industry/Entity Type

Real Estate

Number of Pages Required

2 page

Requirements
Must have
• I don’t want to give too many requirements, because I want to let you all be creative. However, here are the few Must Haves:
• Must submit 2 page designs (a home page and a sub page)
• Must use logo provided
• Focus is mostly on homes, but I would like to include some beach/ocean imagery as well
• The first “item” on the home page should be an accordion/slider which shows pictures of homes and with 1 line of text: “List with the Leader” and two link buttons: “Sell Your Home” and “Buy Your Home”
• Color palette needs to be mainly blues--to match ocean and sky blue
• Exported in all major formats (psd,ai,eps,png,jpeg,etc)
Nice to have
• We don’t necessarily need all of these, but would like to feature most:
• List of videos
• “Meet the Team”—brief team bios and pics
• Link(s) to Blog
• “List with the Leader” – section on why they should choose this firm
• Featured Listings
• Previously Sold

```html
<!DOCTYPE html>
<html lang="en">
<head>
<meta charset="utf-8">
<title>Marlow on the Shore — Oceanfront Real Estate</title>
<link rel="stylesheet" href="https://fonts.googleapis.com/css2?family=Roboto:wght@300;400;500;700&family=Roboto+Condensed:wght@400;700&family=Noto+Serif:wght@700&display=swap">
<style>
:root{
  --ink:#3d3d3d;
  --muted:#666;
  --blue:#0b8bd0;
  --blue-dark:#0a6fa8;
  --orange:#e84a1f;
  --red:#c0281a;
  --sidebar:#efeded;
  --white:#ffffff;
  --line:#cfcfcf;
  --dark:#1c1c1c;
}
*{box-sizing:border-box;margin:0;padding:0}
html,body{width:1200px;height:3226px;overflow:hidden}
body{position:relative;background:var(--white);font-family:"Roboto",Arial,sans-serif;color:var(--ink)}
.abs{position:absolute}
a{color:inherit;text-decoration:none}

/* hero */
.hero{left:0;top:0;width:1200px;height:613px;background:linear-gradient(180deg,#8da7a0 0%,#6f8f63 30%,#5b7a45 48%,#cfc7b6 70%,#9a9487 88%,#4e5a4c 100%)}
.site-header{left:0;top:0;width:1200px;height:133px;background:rgba(255,255,255,.72)}
.brand{left:140px;top:30px;width:170px;font-family:"Roboto",sans-serif;font-weight:300;font-size:30px;line-height:34px;color:#555;text-transform:uppercase;letter-spacing:1px}
.call{left:480px;top:30px;font-family:"Roboto Condensed",sans-serif;font-size:12px;color:#444;display:flex;align-items:center;gap:8px}
.call strong{font-size:21px;font-weight:700;color:#333}
.search{left:752px;top:25px;width:323px;height:32px;border:1px solid #aaa;background:rgba(255,255,255,.6);font-size:12px;color:#666;padding:8px 10px}
.search svg{position:absolute;right:0;top:6px}
.social-mini{left:940px;top:30px;display:flex;gap:12px}
.social-mini span{width:16px;height:16px;background:#444;display:block}
.nav{left:437px;top:80px;display:flex;gap:34px;font-family:"Roboto Condensed",sans-serif;font-size:17px;color:#333;text-transform:uppercase}
.hero-title{left:0;top:288px;width:1200px;text-align:center;font-weight:300;font-size:56px;letter-spacing:3px;color:var(--white)}
.btn-pill{height:36px;border-radius:18px;font-family:"Roboto Condensed",sans-serif;font-size:15px;display:flex;align-items:center;justify-content:center;color:var(--white)}
.btn-sell{left:425px;top:397px;width:163px;border:2px solid var(--white)}
.btn-buy{left:600px;top:397px;width:170px;background:var(--blue)}
.dots{left:568px;top:555px;width:64px;height:20px;background:rgba(0,0,0,.35);border-radius:3px;display:flex;gap:6px;align-items:center;justify-content:center}
.dots i{width:9px;height:9px;border-radius:50%;background:var(--white);display:block}

/* shared */
.section-title{font-weight:300;font-size:38px;letter-spacing:1px;text-transform:uppercase}
.intro{font-size:14px;line-height:22px;width:600px}
.intro a{color:var(--blue);border-bottom:1px solid var(--blue)}
.sidebar{left:785px;top:613px;width:415px;height:2054px;background:var(--sidebar)}
.ph{display:block}
.arrows{display:flex;gap:3px}
.arrows span{width:24px;height:24px;display:flex;align-items:center;justify-content:center}

/* video */
.video-main{left:123px;top:763px;width:447px;height:422px;background:linear-gradient(180deg,#0d0d14,#1d2130 55%,#3a2e1e 85%,#121212)}
.play{left:298px;top:925px}
.watch{left:123px;top:990px;width:447px;text-align:center;font-weight:700;font-size:29px;color:var(--white);letter-spacing:1px}
.video-list{left:570px;top:763px;width:180px;height:422px;background:#111}
.video-list h3{height:47px;background:var(--blue);color:var(--white);font-family:"Noto Serif",serif;font-size:23px;text-align:center;line-height:47px}
.thumb{position:absolute;left:4px;width:176px;height:116px}

/* sidebar widgets */
.side-title{left:785px;top:658px;width:415px;text-align:center;font-weight:300;font-size:24px;line-height:30px;text-transform:uppercase;color:#333}
.promo{left:812px;top:725px;width:262px;height:276px;background:var(--white);border:1px solid var(--line);text-align:center}
.promo h4{font-weight:400;font-size:17px;margin-top:18px}
.promo .date{font-size:10px;color:#999;margin-top:4px}
.promo p{font-size:12px;line-height:16px;color:#555;width:200px;margin:10px auto 0}
.btn-red{display:inline-block;margin-top:10px;background:var(--red);color:var(--white);font-size:10px;padding:4px 12px;border-radius:2px}
.sold{left:812px;top:1045px;width:263px;height:205px}
.sold-head{height:42px;background:var(--blue-dark);display:flex;align-items:center;justify-content:space-between;padding:0 10px 0 18px;color:var(--white);font-family:"Noto Serif",serif;font-size:18px}

/* team */
.team{left:0;top:1230px;width:750px;height:432px;background:var(--blue)}
.team-photo{left:70px;top:1270px;width:290px;height:392px;background:linear-gradient(180deg,#6a8fb0,#5b6a73 50%,#5a5048)}
.team-title{left:383px;top:1290px;color:var(--white);font-weight:300;font-size:36px;letter-spacing:1px}
.team-text{left:383px;top:1345px;width:330px;color:var(--white);font-size:14px;line-height:22px}
.team-text p{margin-bottom:20px}
.btn-outline{left:383px;top:1568px;width:113px;height:32px;border:2px solid var(--white);border-radius:16px;color:var(--white);font-size:11px;display:flex;align-items:center;justify-content:center}
.next{left:635px;top:1576px;color:var(--white);font-size:15px;letter-spacing:1px;display:flex;align-items:center;gap:6px}

/* blog */
.post{width:310px;height:118px;border:1px solid var(--line);background:var(--white)}
.avatar{position:absolute;left:10px;top:10px;width:98px;height:98px;border-radius:50%}
.post p{position:absolute;left:120px;top:14px;width:175px;font-size:11px;line-height:16px;color:#444}
.meta{position:absolute;left:120px;top:82px;font-size:9px;color:#888;display:flex;gap:12px;align-items:center}
.meta b{display:inline-block;width:8px;height:8px;background:#999;margin-right:4px}
.meta b.red{background:var(--red)}

/* featured */
.featured{left:0;top:2090px;width:750px;height:577px;background:var(--orange)}
.featured .section-title{position:absolute;left:123px;top:30px;color:var(--white);font-size:28px}
.featured .intro{position:absolute;left:123px;top:77px;color:var(--white)}
.featured .intro a{color:var(--white);border-color:var(--white)}
.listing-main{left:123px;top:2233px;width:445px;height:385px;background:linear-gradient(180deg,#6d5a4a,#3b2c22 40%,#b07a3a 60%,#3a2516)}
.listing-cap{left:123px;top:2518px;width:445px;height:100px;background:rgba(0,0,0,.55);color:var(--white);padding:10px 24px}
.listing-cap h5{font-family:"Noto Serif",serif;font-size:16px}
.listing-cap p{font-size:11px;line-height:15px;margin-top:6px}
.listing-side{left:568px;top:2233px;width:162px;height:385px;background:var(--dark)}
.listing-side .ph{position:absolute;left:19px;width:128px;height:120px}
.listing-side h6{position:absolute;left:19px;font-family:"Noto Serif",serif;font-size:14px;color:var(--white)}
.listing-side small{position:absolute;left:19px;font-size:10px;color:#ddd}

/* map */
.map{left:0;top:2667px;width:1200px;height:413px;background:linear-gradient(90deg,#e8e3d8,#ebe7dc 60%,#cfdcc0 85%,#b9d0a8)}
.map-card{left:395px;top:2780px;width:332px;height:195px;background:var(--white);box-shadow:0 1px 4px rgba(0,0,0,.3)}
.map-card .ph{height:100px;background:linear-gradient(180deg,#5a6672,#2e3238)}
.map-brand{position:absolute;left:14px;top:80px;width:86px;height:82px;background:#e9e9e9;padding:8px;font-size:13px;line-height:16px;color:#555;text-transform:uppercase}
.map-name{position:absolute;left:115px;top:78px;color:var(--white);font-weight:700;font-size:15px}
.map-line{position:absolute;left:115px;font-size:13px;color:#333;display:flex;gap:6px;align-items:center}

/* footer */
.footer-social{left:460px;top:3110px;display:flex;gap:8px}
.footer-social span{width:50px;height:50px;border-radius:6px;display:block}
.copyright{left:0;top:3176px;width:1200px;text-align:center;font-size:13px;color:#444}
</style>
</head>
<body>

<section class="hero abs" role="img" aria-label="Photo of a clifftop estate terrace with balustrades, pool and gardens"></section>

<header class="site-header abs">
  <div class="brand abs">Marlow on the Shore</div>
  <div class="call abs">CALL US TODAY
    <svg width="20" height="16" viewBox="0 0 20 16"><path d="M2 6c0-3 16-3 16 0v2h-4V6H6v2H2z M5 9h10l2 6H3z" fill="#333"/></svg>
    <strong>555-014-2290</strong></div>
  <div class="search abs">Search
    <svg width="20" height="20" viewBox="0 0 20 20"><circle cx="8" cy="8" r="5" fill="none" stroke="#333" stroke-width="2"/><path d="M12 12l5 5" stroke="#333" stroke-width="2"/></svg>
  </div>
  <div class="social-mini abs" aria-label="Social links"><span></span><span></span><span></span><span></span></div>
  <nav class="nav abs"><a>Home</a><a>Sell</a><a>Property Search</a><a>Team</a><a>Videos</a><a>Blog</a><a>Contact</a></nav>
</header>

<h1 class="hero-title abs">LIST WITH THE LEADER</h1>
<a class="btn-pill btn-sell abs">SELL YOUR HOME</a>
<a class="btn-pill btn-buy abs">BUY YOUR HOME</a>
<div class="dots abs"><i></i><i></i><i></i></div>

<aside class="sidebar abs"></aside>

<h2 class="section-title abs" style="left:123px;top:645px;color:#555">Our Video</h2>
<p class="intro abs" style="left:123px;top:690px">Lorem Ipsum is simply dummy text of the printing indus try. Lorem Ipsum standard Lorem Ipsum standard dummy text. <a>Read More</a></p>

<div class="video-main abs" role="img" aria-label="Night city skyline video still"></div>
<svg class="play abs" width="56" height="56" viewBox="0 0 56 56"><circle cx="28" cy="28" r="27" fill="#fff"/><path d="M22 16l18 12-18 12z" fill="#111"/></svg>
<div class="watch abs">WATCH INTRO VIDEO</div>
<div class="arrows abs" style="left:502px;top:1160px"><span style="background:#fff"><svg width="8" height="10"><path d="M7 0L1 5l6 5" fill="none" stroke="#333" stroke-width="2"/></svg></span><span style="background:var(--red)"><svg width="8" height="10"><path d="M1 0l6 5-6 5" fill="none" stroke="#fff" stroke-width="2"/></svg></span></div>
<div class="video-list abs">
  <h3>Hotels</h3>
  <div class="thumb ph" style="top:51px;background:linear-gradient(180deg,#1f3550,#c08a3a)" role="img" aria-label="Aerial city lights at dusk"></div>
  <div class="thumb ph" style="top:171px;background:linear-gradient(180deg,#0e1420,#5a4a2a)" role="img" aria-label="City lights at night"></div>
  <div class="thumb ph" style="top:291px;background:linear-gradient(180deg,#6a5a44,#d8c9a8)" role="img" aria-label="Hotel lobby interior"></div>
</div>

<h2 class="side-title abs">List with the<br>Leader</h2>
<div class="promo abs">
  <h4>Lorem Ipsum is simply</h4>
  <div class="date">Feb 11, 2015 5:53 AM</div>
  <div class="ph" style="width:120px;height:80px;margin:12px auto 0;background:radial-gradient(circle,#d8322a 0%,#e8e8e8 70%)" role="img" aria-label="Illustration of gears with a free to join sign"></div>
  <p>Lorem Ipsum is simply dummy text of the printing indus try. Lorem Ipsum standard Lorem Ipsum standard</p>
  <span class="btn-red">Read More</span>
</div>
<div class="sold abs">
  <div class="sold-head">Previously Sold
    <div class="arrows"><span style="width:16px;height:16px;background:#fff"><svg width="6" height="8"><path d="M5 0L1 4l4 4" fill="none" stroke="#333" stroke-width="1.5"/></svg></span><span style="width:16px;height:16px;background:var(--red)"><svg width="6" height="8"><path d="M1 0l4 4-4 4" fill="none" stroke="#fff" stroke-width="1.5"/></svg></span></div>
  </div>
  <div class="ph" style="height:163px;background:linear-gradient(90deg,#9fb4c4,#7a8a94 50%,#c9c2b4)" role="img" aria-label="Photo of an agent at her desk"></div>
</div>

<section class="team abs"></section>
<div class="team-photo abs" role="img" aria-label="Portrait of the lead agent in a grey suit"></div>
<h2 class="team-title abs">TEAM</h2>
<div class="team-text abs">
  <p>Lorem Ipsum is simply dummy text.</p>
  <p>Lorem Ipsum is simply dummy text of the printing industry. Lorem Ipsum standard dummy text. Lorem Ipsum is simply dummy text of the printing industry. Lorem Ipsum standard dummy text.</p>
  <p>Lorem Ipsum is simply dummy text of the printing industry. Lorem Ipsum standard dummy text. Lorem Ipsum is simply dummy text.</p>
</div>
<a class="btn-outline abs">READ MORE</a>
<div class="next abs"><svg width="8" height="12"><path d="M7 1L2 6l5 5" fill="none" stroke="#fff" stroke-width="2"/></svg>NEXT<svg width="8" height="12"><path d="M1 1l5 5-5 5" fill="none" stroke="#fff" stroke-width="2"/></svg></div>

<h2 class="section-title abs" style="left:123px;top:1695px;color:#555">Blog</h2>
<p class="intro abs" style="left:123px;top:1742px">Lorem Ipsum is simply dummy text of the printing indus try. Lorem Ipsum standard Lorem Ipsum standard dummy text. <a>Read More</a></p>

<article class="post abs" style="left:123px;top:1806px"><div class="avatar ph" style="background:linear-gradient(180deg,#c9a66b,#6f8fa8)" role="img" aria-label="Author photo"></div><p>Lorem Ipsum is simply dummy text of the printing and typesetting industry.</p><div class="meta"><span><b></b>By : Jordan M Ellis</span><span><b class="red"></b>May 1, 2015</span></div></article>
<article class="post abs" style="left:444px;top:1806px"><div class="avatar ph" style="background:linear-gradient(180deg,#5a4030,#d9c8b8)" role="img" aria-label="Author photo"></div><p>Lorem Ipsum is simply dummy text of the printing and typesetting industry.</p><div class="meta"><span><b></b>By : Jordan M Ellis</span><span><b class="red"></b>May 1, 2015</span></div></article>
<article class="post abs" style="left:123px;top:1928px"><div class="avatar ph" style="background:linear-gradient(180deg,#2a201a,#d8c0a8)" role="img" aria-label="Author photo"></div><p>Lorem Ipsum is simply dummy text of the printing and typesetting industry.</p><div class="meta"><span><b></b>By : Jordan M Ellis</span><span><b class="red"></b>May 1, 2015</span></div></article>
<article class="post abs" style="left:444px;top:1928px"><div class="avatar ph" style="background:linear-gradient(180deg,#8a8a8a,#4a5058)" role="img" aria-label="Author photo"></div><p>Lorem Ipsum is simply dummy text of the printing and typesetting industry.</p><div class="meta"><span><b></b>By : Jordan M Ellis</span><span><b class="red"></b>May 1, 2015</span></div></article>

<section class="featured abs">
  <h2 class="section-title">Featured Listings</h2>
  <p class="intro">Lorem Ipsum is simply dummy text of the printing indus try. Lorem Ipsum standard Lorem Ipsum standard dummy text. <a>Read More</a></p>
</section>
<div class="listing-main abs" role="img" aria-label="Candlelit beachfront dining terrace at dusk"></div>
<div class="listing-cap abs">
  <h5>Lorem Ipsum available,</h5>
  <p>There are many variatio passages of Lorem. Ipsum available the majority have suffered alteration in some form, by injected humour, or randomised words which don't look even slightly believable.</p>
</div>
<div class="arrows abs" style="left:506px;top:2588px"><span style="background:#fff"><svg width="8" height="10"><path d="M7 0L1 5l6 5" fill="none" stroke="#333" stroke-width="2"/></svg></span><span style="background:var(--red)"><svg width="8" height="10"><path d="M1 0l6 5-6 5" fill="none" stroke="#fff" stroke-width="2"/></svg></span></div>
<div class="listing-side abs">
  <div class="ph" style="top:18px;background:linear-gradient(180deg,#4a2a6a,#c04a9a)" role="img" aria-label="Nightlife venue photo"></div>
  <h6 style="top:148px">Lorem Ipsum</h6><small style="top:168px">There are many variatio.</small>
  <div class="ph" style="top:196px;background:linear-gradient(180deg,#6a5a44,#d8c09a)" role="img" aria-label="Luxury bedroom interior"></div>
  <h6 style="top:326px">Lorem Ipsum</h6><small style="top:346px">There are many variatio.</small>
</div>

<section class="map abs" role="img" aria-label="Map of Southern California showing the office location"></section>
<div class="map-card abs">
  <div class="ph" role="img" aria-label="Oceanfront home exterior at dusk"></div>
  <div class="map-brand">Marlow on the Shore</div>
  <div class="map-name">Marlow on the Shore</div>
  <div class="map-line" style="top:118px"><svg width="10" height="14" viewBox="0 0 10 14"><path d="M5 0a5 5 0 0 1 5 5c0 4-5 9-5 9S0 9 0 5a5 5 0 0 1 5-5z" fill="#333"/><circle cx="5" cy="5" r="2" fill="#fff"/></svg>xxxx Southern California, USA.</div>
  <div class="map-line" style="top:145px"><svg width="12" height="12" viewBox="0 0 12 12"><path d="M2 0l3 3-1.5 2a7 7 0 0 0 3.5 3.5L9 7l3 3-2 2C5 12 0 7 0 2z" fill="#333"/></svg>555 014 2290</div>
</div>

<div class="footer-social abs" aria-label="Social links">
  <span style="background:#3b5a9a"></span><span style="background:#c9282d"></span><span style="background:#3aa8e0"></span><span style="background:#3a4a62"></span><span style="background:#5a4436"></span>
</div>
<p class="copyright abs">Copyright © 2015 - Marlow on the Shore.com</p>

</body>
</html>
```